A5 Flyer for mobile App development

We need a double sided flyer design that will need to be printed on A5 sized paper.
The design will be based on a phone/tablet look and feel.

The idea behind the pamphlet is that we show clients that they can have a mobile app white labelled to their company/brand.

The front of the pamphlet will need to look like a front of a phone with a generic mobile app running within the phone.
The phone must not resemble a real phone, however, it should resemble a cartoon look phone - similar to the attached image called "phone.jpg". The mobile app running within the phone needs to have a "drawing/wireframe" look - similar to the "mock.jpg" image attached. The logo part should look like a "placeholder" image - similar to the image named "mocklogo" (look at the far left) attached.

The back of the pamphlet must also be similar, so that when you turn over the pamphlet, it should look like you're turning over a real phone, and you're now the seeing the back of the phone.
The back of the phone should be styled similar to the front. The text and items on the back of the phone are also in the image named "20170503_212415.jpg".

The phone on the pamphlet should not have an outline, meaning that the pamphlet will have rounded corners, giving the phone a shape.

Please send us a message if you're unsure about anything.

Target Market(s)

Businesses that have salons, spa's, beauty clinics, etc.

Industry/Entity Type

Health And Wellness

Font styles to use
Sans Serif
Script

Colors
e34297

Requirements
Must have
• The pamphlet will have rounded corners, giving the phone its look. See attached the image named "pingloom.."
Should not have
• the phone on the pamphlet should not have an outline, meaning that the pamphlet will have rounded corners, giving the phone a shape. Please have a look at the pingloom image attached that demonstrates the cut out lines.

```html
<!DOCTYPE html>
<html lang="en">
<head>
<meta charset="utf-8">
<title>Glowbook A5 App Flyer – Front and Back</title>
<link rel="stylesheet" href="https://fonts.googleapis.com/css2?family=Archivo+Black&family=Patrick+Hand&family=Raleway:wght@300;400;700;800&display=swap">
<style>
  :root {
    --stage: #2b2b2b;
    --front-body: #f4f6f8;
    --front-edge: #dcdfe3;
    --bar: #111111;
    --screen-top: #e6f6fd;
    --screen-bottom: #3fcdf7;
    --ink: #444a4f;
    --ink-dark: #1c1c1c;
    --box-line: #7f9aa8;
    --cta-top: #42d67c;
    --cta-bottom: #1cb457;
    --white: #ffffff;
    --back-light: #ececec;
    --back-dark: #a9a9a9;
    --brand-pink: #e34297;
    --badge: #1e1e1e;
    --badge-line: #9a9a9a;
    --back-line: #8c8c8c;
  }
  * { box-sizing: border-box; margin: 0; padding: 0; }
  html, body { width: 1200px; height: 771px; overflow: hidden; }
  body { background: var(--stage); position: relative; font-family: "Raleway", sans-serif; }

  .flyer-side { position: absolute; top: 45px; width: 456px; height: 681px; border-radius: 40px; }

  /* Front */
  .flyer-front { left: 99px; background: var(--front-body); box-shadow: inset 0 0 0 3px var(--front-edge); }
  .front-camera { position: absolute; left: 222px; top: 32px; width: 10px; height: 10px; border-radius: 50%; background: #222; }
  .app-screen {
    position: absolute; left: 22px; top: 66px; width: 412px; height: 549px;
    background: linear-gradient(165deg, var(--screen-top) 0%, #bfeafb 55%, var(--screen-bottom) 100%);
    border: 2px solid var(--bar); overflow: hidden;
  }
  .status-bar {
    height: 14px; background: var(--bar); color: var(--white);
    font-size: 7px; display: flex; align-items: center; justify-content: center; position: relative;
  }
  .status-bar .signal { position: absolute; left: 6px; top: 3px; }
  .status-bar .battery { position: absolute; right: 8px; top: 4px; width: 11px; height: 6px; background: var(--white); border-radius: 1px; }
  .store-mark { position: absolute; left: 0; right: 0; top: 50px; text-align: center; }
  .store-mark .mark-square { width: 60px; height: 60px; margin: 0 auto 42px; background: #2f8fd1; border-radius: 4px; }
  .store-name { font-weight: 700; font-size: 21px; color: var(--ink); line-height: 1; }
  .store-sub { font-size: 7px; letter-spacing: 1.5px; color: var(--ink); margin-top: 3px; }
  .brand-placeholder {
    position: absolute; left: 37px; top: 246px; width: 337px; height: 139px;
    border: 1px solid var(--box-line); border-radius: 6px;
    display: flex; align-items: center; justify-content: center;
    font-weight: 700; font-size: 30px; color: var(--ink); letter-spacing: -0.5px;
  }
  .book-now {
    position: absolute; left: 78px; top: 449px; width: 255px; height: 40px;
    background: linear-gradient(var(--cta-top), var(--cta-bottom)); border-radius: 3px;
    display: flex; align-items: center; justify-content: center;
    font-weight: 700; font-size: 28px; color: var(--white);
  }
  .pointer { position: absolute; left: 204px; top: 26px; width: 24px; height: 28px; }
  .home-button { position: absolute; left: 210px; top: 630px; width: 36px; height: 36px; border-radius: 50%; border: 1px solid var(--front-edge); }

  /* Back */
  .flyer-back { left: 630px; background: radial-gradient(ellipse at 50% 45%, var(--back-light) 0%, #d6d6d6 55%, var(--back-dark) 100%); }
  .back-mic { position: absolute; left: 225px; top: 38px; width: 6px; height: 2px; background: #333; }
  .back-brand {
    position: absolute; left: 0; right: 0; top: 118px;
    display: flex; align-items: center; justify-content: center; gap: 12px;
    font-family: "Archivo Black", sans-serif; font-size: 50px; color: var(--ink-dark); letter-spacing: -1px;
  }
  .back-brand .mark-square { width: 34px; height: 34px; background: var(--brand-pink); }
  .price-line { position: absolute; left: 0; right: 0; top: 240px; text-align: center; font-family: "Patrick Hand", cursive; font-size: 46px; color: var(--ink-dark); }
  .pitch-box {
    position: absolute; left: 60px; top: 342px; width: 338px; height: 113px;
    border: 1px solid var(--back-line); border-radius: 3px;
    display: flex; align-items: center; justify-content: center; text-align: center;
    font-weight: 800; font-size: 21px; line-height: 27px; color: var(--ink-dark); letter-spacing: -0.4px;
  }
  .store-badges { position: absolute; left: 94px; top: 523px; display: flex; gap: 18px; }
  .store-badge { width: 126px; height: 40px; background: var(--badge); border: 1px solid var(--badge-line); border-radius: 4px; }
  .contact-email { position: absolute; left: 0; right: 0; top: 598px; text-align: center; font-size: 21px; color: var(--ink-dark); }
</style>
</head>
<body>
  <section class="flyer-side flyer-front" aria-label="Flyer front">
    <div class="front-camera"></div>
    <div class="app-screen">
      <div class="status-bar">
        <svg class="signal" width="22" height="8" viewBox="0 0 22 8"><path d="M0 8 L6 2 L6 8Z M8 8 L14 2 L14 8Z" fill="#fff"/><circle cx="19" cy="6" r="1.5" fill="#fff"/></svg>
        10:03 AM
        <span class="battery"></span>
      </div>
      <div class="store-mark">
        <div class="mark-square"></div>
        <div class="store-name">Handset Hub</div>
        <div class="store-sub">STORE</div>
      </div>
      <div class="brand-placeholder">YOUR BRAND HERE</div>
      <div class="book-now">BOOK NOW
        <svg class="pointer" viewBox="0 0 24 28"><path d="M8 2 a2 2 0 0 1 4 0 V12 h1 V10 a2 2 0 0 1 4 0 v3 a2 2 0 0 1 4 0 v7 c0 4 -3 7 -7 7 h-3 c-3 0 -5 -2 -7 -5 L1 17 a2 2 0 0 1 3 -2 l4 4 Z" fill="#fff" stroke="#222" stroke-width="1.3"/></svg>
      </div>
    </div>
    <div class="home-button"></div>
  </section>

  <section class="flyer-side flyer-back" aria-label="Flyer back">
    <div class="back-mic"></div>
    <div class="back-brand"><span class="mark-square"></span>GLOWBOOK</div>
    <div class="price-line">Fromr499pm</div>
    <div class="pitch-box">LET YOUR CUENTS BOOK<br>THEIE NEXT APPOINTMENT<br>USING YOUR APP</div>
    <div class="store-badges">
      <div class="store-badge"></div>
      <div class="store-badge"></div>
    </div>
    <div class="contact-email">Email-info@glowbookmail.com</div>
  </section>
</body>
</html>
```